Logo needed for business card

Velquist Pty Ltd is in the business of healthcare and ecommerce.

We own and manage pharmacies and online health ecomerce sites.

We provide ecommerce consultants for companies looking for an ecommerce business startegy.

Think of it as the umbrella under which several healthcare brands may sit.

When I think of Velquist, I visulaise slick black/metalic colours, so please stay away from the common blue and green colours that seem to be so popular in this field.

Target Market(s)

CEOs and COOs

Industry/Entity Type

Healthcare

Contact Information for Business Card

Tessa Lindqvist
Director
Velquist Pty Ltd
4/362 Fennick Pde
Brellton, NSW 2148

Requirements
Must have
• Design must have scope to be implemented on the company's website and letterheads etc.

```html
<!DOCTYPE html>
<html lang="en">
<head>
<meta charset="utf-8">
<title>Velquist Pty Ltd — Business Card</title>
<link rel="stylesheet" href="https://fonts.googleapis.com/css2?family=Questrial&display=swap">
<style>
  :root {
    --backdrop: #e4e4e2;
    --metal-light: #f1f1f1;
    --metal-mid: #d9d9d9;
    --metal-dark: #bdbdbd;
    --ink: #1e1e1e;
    --ink-soft: #3a3a3a;
    --rule: #4a4a4a;
    --mark: #5a5a5a;
  }
  * { margin: 0; padding: 0; box-sizing: border-box; }
  html, body {
    width: 1200px;
    height: 900px;
    overflow: hidden;
    background: var(--backdrop);
    font-family: "Questrial", "Century Gothic", sans-serif;
    color: var(--ink);
  }
  .canvas {
    width: 1200px;
    height: 900px;
    display: flex;
    align-items: center;
    justify-content: center;
  }
  .business-card {
    position: relative;
    width: 840px;
    height: 480px;
    border-radius: 34px;
    background:
      repeating-linear-gradient(0deg, rgba(255,255,255,0.18) 0 1px, rgba(0,0,0,0.035) 1px 2px, transparent 2px 3px),
      linear-gradient(160deg, var(--metal-light) 0%, var(--metal-mid) 45%, var(--metal-light) 70%, var(--metal-dark) 100%);
    box-shadow: 0 18px 40px rgba(0,0,0,0.25), inset 0 1px 0 rgba(255,255,255,0.8);
  }
  .brand {
    position: absolute;
    left: 120px;
    top: 92px;
    display: flex;
    align-items: center;
    gap: 22px;
  }
  .brand-dot {
    width: 64px;
    height: 64px;
    border-radius: 50%;
    background: var(--mark);
  }
  .brand-name {
    font-size: 84px;
    line-height: 1;
    letter-spacing: 1px;
    color: var(--mark);
  }
  .tagline {
    position: absolute;
    left: 206px;
    top: 190px;
    font-size: 17px;
    letter-spacing: 0.3px;
    color: var(--ink-soft);
  }
  .person {
    position: absolute;
    left: 150px;
    top: 318px;
    text-align: center;
  }
  .person-name {
    font-size: 28px;
    color: var(--ink);
  }
  .person-role {
    font-size: 15px;
    color: var(--ink-soft);
    margin-top: 2px;
  }
  .company-details {
    position: absolute;
    left: 500px;
    top: 248px;
    padding-left: 22px;
    border-left: 1.5px solid var(--rule);
    height: 92px;
    font-size: 17px;
    line-height: 1.35;
    color: var(--ink-soft);
  }
</style>
</head>
<body>
  <main class="canvas">
    <section class="business-card" aria-label="Velquist business card">
      <div class="brand">
        <span class="brand-dot" aria-hidden="true"></span>
        <span class="brand-name">Velquist</span>
      </div>
      <p class="tagline">Ecommerce - Health - Strategy - Consulting</p>

      <div class="person">
        <p class="person-name">Tessa Lindqvist</p>
        <p class="person-role">Director</p>
      </div>

      <address class="company-details" style="font-style: normal;">
        <p>Velquist Pty Ltd</p>
        <p>4/362 Fennick Pde Brellton, NSW 2148</p>
      </address>
    </section>
  </main>
</body>
</html>
```